Design a Hemp Museum + exhibition design**

I'm creating an Online Museum for Hemp which will tell the story of hemp from ancient times to now and the future
cover the medical, industrial and nutritional uses and development of hemp
the people behind it, researchers, politicians, farmers and influencerts

the museum will have a number of "wings" , each holds an exhibition around a differnet theme, for example:

Hemp in the Age of Empires: 18th and 19th Century Collections
Hemp - The History of Healing
Domestication and Early Use: Ancient Collection
From Cotton Gin to Plastics and Prohibition: Hemp's Decline

these are just a few sample ideas for exhibitions

I'm looking for an overall design for the museum home page and exhibition page which will make people curious and want to spend time,learning and browsing

Think mobile -first :)

You are requested to design

1. Home page
2. Exhibition page

Target Market(s)

Hemp aficionados, curious fans

Logo Text

The Lumen Museum

Coding

Coded - Design and coding required

Number of Pages Required

3 page

Font styles to use
Sans Serif
Decorative

Requirements
Must have
• a homepage design which prompts visitors to immediately start watching an exhibition

visitors need to understand that this is a museum , so that they dont think it's a business, a service provider or anything like that

needs to have the usual links to T&C, privacy, about us

needs to have a link to "Wander past the lantern stall"

must have a visual WOW effect
Nice to have
• animations, sounds etc
Should not have
• forms like contact us etc - not relevant

```html
<!DOCTYPE html>
<html lang="en">
<head>
<meta charset="UTF-8">
<title>The Lumen Museum — Exhibit 02</title>
<link rel="stylesheet" href="https://fonts.googleapis.com/css2?family=Playfair+Display:wght@400;700&family=Oswald:wght@500&display=swap">
<style>
  :root {
    --header-tan: #c4a571;
    --page-sand: #d8bb8a;
    --fibre-dark: #3b2f22;
    --fibre-mid: #6e5a40;
    --fibre-light: #a88a5e;
    --glass: rgba(122, 108, 92, 0.72);
    --ink-light: #ffffff;
    --ink-dark: #1b1712;
    --leaf-green: #1f4a0c;
    --leaf-bright: #3f7a22;
  }
  * { margin: 0; padding: 0; box-sizing: border-box; }
  html, body { width: 1200px; height: 675px; overflow: hidden; }
  body {
    position: relative;
    background: var(--page-sand);
    font-family: "Playfair Display", Georgia, serif;
    color: var(--ink-light);
  }
  .site-header {
    position: absolute; left: 0; top: 0; width: 1200px; height: 85px;
    background: var(--header-tan);
    border-bottom: 1px solid rgba(80, 60, 30, 0.35);
    box-shadow: 0 2px 10px rgba(60, 40, 10, 0.15);
    z-index: 5;
  }
  .brand {
    position: absolute; left: 89px; top: 29px;
    font-size: 21px; font-weight: 700; letter-spacing: 0.2px;
  }
  .main-nav a {
    position: absolute; top: 34px;
    font-size: 13px; font-weight: 700; color: var(--ink-light);
    text-decoration: none; transform: translateX(-50%);
    white-space: nowrap;
  }
  .main-nav .nav-cta {
    top: 22px; left: 682px; width: 162px; height: 41px;
    border: 2px solid var(--ink-light);
    display: flex; align-items: center; justify-content: center;
  }
  .green-disc {
    position: absolute; left: -90px; top: 511px;
    width: 340px; height: 340px; border-radius: 50%;
    background: var(--leaf-green);
  }
  .exhibit-stage {
    position: absolute; left: 88px; top: 116px; width: 1025px; height: 528px;
    box-shadow: 0 14px 34px rgba(50, 35, 15, 0.45);
    overflow: hidden;
  }
  .stage-photo {
    position: absolute; inset: 0;
    background:
      radial-gradient(ellipse at 30% 40%, rgba(168,138,94,0.55), transparent 55%),
      radial-gradient(ellipse at 75% 70%, rgba(140,112,76,0.5), transparent 60%),
      linear-gradient(135deg, var(--fibre-mid), var(--fibre-dark) 55%, var(--fibre-mid));
  }
  .exhibit-number {
    position: absolute; left: 2px; top: -8px;
    font-family: "Oswald", "Arial Narrow", sans-serif; font-weight: 500;
    font-size: 118px; line-height: 1; letter-spacing: -2px;
    color: transparent; -webkit-text-stroke: 1px var(--ink-light);
  }
  .exhibit-label {
    position: absolute; left: 135px; top: 25px;
    font-family: "Oswald", "Arial Narrow", sans-serif; font-weight: 500;
    font-size: 52px; line-height: 1; letter-spacing: -1px;
    color: transparent; -webkit-text-stroke: 1px var(--ink-light);
  }
  .exhibit-title {
    position: absolute; left: 35px; top: 203px; width: 470px;
    font-size: 40px; font-weight: 700; line-height: 42px;
  }
  .story-card {
    position: absolute; left: 512px; top: 56px; width: 469px; height: 416px;
    background: var(--glass);
    backdrop-filter: blur(14px);
    padding: 27px 27px 0 27px;
  }
  .story-card h2 {
    font-size: 22.5px; font-weight: 400; line-height: 31px; width: 370px;
  }
  .key-info {
    display: inline-flex; align-items: center; gap: 6px;
    margin-top: 61px;
    font-size: 15px; color: var(--ink-dark); text-decoration: none;
  }
  .story-text {
    margin-top: 49px; width: 405px;
    font-size: 15px; line-height: 22px;
  }
  .leaf-photo {
    position: absolute; left: 960px; top: 460px; width: 230px; height: 200px;
    background: radial-gradient(ellipse at 55% 55%, var(--leaf-bright) 0%, var(--leaf-green) 40%, rgba(31,74,12,0) 70%);
    z-index: 3;
  }
</style>
</head>
<body>
  <header class="site-header">
    <div class="brand">The Lumen Museum</div>
    <nav class="main-nav">
      <a class="nav-cta" href="#">See Exhibitions</a>
      <a href="#" style="left:827px">About Us</a>
      <a href="#" style="left:966px">Privacy Policy</a>
      <a href="#" style="left:1097px">T &amp; C</a>
    </nav>
  </header>

  <div class="green-disc"></div>

  <main class="exhibit-stage">
    <div class="stage-photo" role="img" aria-label="Close-up photograph of tangled raw hemp fibres"></div>
    <div class="exhibit-number">02</div>
    <div class="exhibit-label">Exhibit</div>
    <h1 class="exhibit-title">Hemp in Modern Industry: As a food, textile and biofuel</h1>

    <section class="story-card">
      <h2>Back in Production: if you build it they will come As a food As a textile</h2>
      <a class="key-info" href="#">Key Info
        <svg width="22" height="10" viewBox="0 0 22 10" aria-hidden="true"><path d="M0 5H20M15 1L20 5L15 9" fill="none" stroke="#1b1712" stroke-width="1.3"/></svg>
      </a>
      <p class="story-text">The French Resistance: still growing during prohibition despite UN pressure In 2000, highly controlled hemp returned to US stores as a&nbsp; China's Great Leap Forward to dominate textile production including (banned elsewhere) hemplegal food good&nbsp; China's Great Leap Forward to dominate textile production including (banned elsewhere) hemp</p>
    </section>
  </main>

  <div class="leaf-photo" role="img" aria-label="Photograph of a green hemp leaf"></div>
</body>
</html>
```